Fieldcrafters new logo business card

We need a business card designed to promote the new direction of our company. Originally (for the past 12 years) we were a design-based marketing consultancy specialising in B2B. But now we are offering marketing consultancy to companies in the ecommerce business. We have expertise in this and operate three online stores ourselves and can provide warehousing and distribution services.
The new logo and business card should reflect this market - e.g. modern, technical, commercial but also creative!
Our current logo is too 'designery' and doesn't reflect the seriousness and professionalism of our current business. It also is very long and thin so doesnot work well in rectangular panels.
The name 'Fieldcrafters' comprises two parts - Field and Crafters and these parts of the word can have a different type font or colour. The 'Field' element is the creative element while the 'Crafters' part is the technical, businesslike part. We can also look at 'The Fieldcrafters Company' rather than just 'fieldcrafters.' We can also include the slogan 'Source, Sell, Succeed.' under the logo.
The address details for the card are 4 Wrenfold Rise, Woking, Surrey GU19 3LT. We will also need an email address and phone number (details will be supplied later)
On the back of the card will be a list of services offered.
Fieldcrafters can help your business succeed through:
Product Sourcing
Marketing
Distribution
Storage
Ecommerce

Target Market(s)

Owners of small and medium-sized retail businesses - particularly mail order and ecommerce based businesses.

Industry/Entity Type

Marketing

Requirements
Must have
• The company name should be prominent. This can either be 'Fieldcrafters' or 'The Fieldcrafters Company'.
• Then the words 'Fieldcrafters Ltd, Unit F, Marlow Vale Park, Copperleaf Road, Elmstead, Woking, Surrey GU21 4RB
• 0844 312 9087 www.thefieldcrafters-example.co.uk
• Must also include cardholder's name and title.
• Martin Hollis
• Director
• On the reverse it should say.
• Fieldcrafters - Developing profitable brands in a multi-channel environment

```html
<!DOCTYPE html>
<html lang="en">
<head>
<meta charset="utf-8">
<title>Fieldcrafters business card</title>
<link rel="stylesheet" href="https://fonts.googleapis.com/css2?family=Tinos:wght@400;700&display=swap">
<style>
  :root {
    --navy: #233a73;
    --red: #e53232;
    --white: #ffffff;
    --paper: #f6f6f6;
    --backdrop: #1f1f1f;
  }
  html, body {
    margin: 0;
    width: 1200px;
    height: 899px;
    overflow: hidden;
    background: var(--backdrop);
  }
  .stage {
    position: relative;
    width: 1200px;
    height: 899px;
  }
  .card {
    position: absolute;
    left: 320px;
    width: 560px;
    height: 320px;
    box-shadow: 0 10px 30px rgba(0,0,0,.55);
  }
  .card--reverse { top: 100px; }
  .card--front { top: 479px; }
  .card svg { display: block; width: 560px; height: 320px; }
  .wordmark { font-family: "Tinos", "Times New Roman", serif; font-size: 36px; fill: var(--navy); letter-spacing: 1px; }
  .headline { font-family: "Tinos", serif; font-weight: 700; font-size: 13px; fill: var(--white); letter-spacing: .5px; }
  .service { font-family: "Tinos", serif; font-size: 16px; fill: var(--white); }
  .holder-name { font-family: "Tinos", serif; font-weight: 700; font-size: 17px; fill: var(--white); letter-spacing: .5px; }
  .holder-title { font-family: "Tinos", serif; font-weight: 700; font-size: 14px; fill: var(--white); }
  .contact { font-family: "Tinos", serif; font-size: 14px; fill: var(--navy); }
  .icon { fill: var(--navy); }
  .icon-line { fill: none; stroke: var(--navy); }
</style>
</head>
<body>
<main class="stage">

  <section class="card card--reverse" aria-label="Card reverse: services">
    <svg viewBox="0 0 560 320" xmlns="http://www.w3.org/2000/svg">
      <rect class="card-base" width="560" height="320" fill="var(--paper)"/>
      <path class="panel-navy" d="M0 0 H420 Q250 230 0 300 Z" fill="var(--navy)"/>
      <path class="swoosh-red" d="M420 0 H560 V40 Q330 240 0 305 L0 300 Q250 230 420 0 Z" fill="var(--red)"/>
      <text class="headline" x="26" y="38">DEVELOPING PROFITABLE BRANDS THROUGH</text>
      <g class="service-list">
        <text class="service" x="46" y="68">Product Sourcing</text>
        <text class="service" x="46" y="88">Marketing</text>
        <text class="service" x="46" y="108">Distribution</text>
        <text class="service" x="46" y="128">Storage</text>
        <text class="service" x="46" y="148">Ecommerce</text>
      </g>
      <text class="wordmark" x="300" y="278">Fieldcrafters</text>
    </svg>
  </section>

  <section class="card card--front" aria-label="Card front: contact details">
    <svg viewBox="0 0 560 320" xmlns="http://www.w3.org/2000/svg">
      <rect class="card-base" width="560" height="320" fill="var(--white)"/>
      <path class="band-navy-top" d="M0 0 H560 V92 Q460 78 270 40 Q120 14 0 12 Z" fill="var(--navy)"/>
      <path class="panel-navy" d="M0 96 L310 138 Q130 172 0 236 Z" fill="var(--navy)"/>
      <path class="swoosh-red" d="M0 258 Q160 170 545 122 Q260 170 95 320 H0 Z" fill="var(--red)"/>
      <text class="wordmark" x="28" y="66">Fieldcrafters</text>
      <text class="holder-name" x="24" y="142">MARTIN HOLLIS</text>
      <text class="holder-title" x="90" y="162">Director</text>
      <g class="contact-list">
        <path class="icon" d="M210 210 l8 -7 l8 7 h-3 v7 h-3 v-4 h-4 v4 h-3 v-7 Z"/>
        <text class="contact" x="234" y="217">4 Wrenfold Rise, Woking, Surrey GU19 3LT</text>
        <rect class="icon" x="211" y="230" width="13" height="9" rx="2"/>
        <rect class="icon" x="209" y="227" width="17" height="3" rx="1.5"/>
        <text class="contact" x="234" y="239">01483 620947</text>
        <rect class="icon" x="392" y="228" width="8" height="13" rx="1.5"/>
        <text class="contact" x="406" y="239">07700 900318</text>
        <rect class="icon-line" x="210" y="250" width="16" height="11" stroke-width="1.6"/>
        <path class="icon-line" d="M210 250 l8 6 l8 -6" stroke-width="1.6"/>
        <text class="contact" x="234" y="261">martin@thefieldcrafters-example.co.uk</text>
        <circle class="icon-line" cx="218" cy="278" r="7" stroke-width="1.4"/>
        <ellipse class="icon-line" cx="218" cy="278" rx="3" ry="7" stroke-width="1.2"/>
        <path class="icon-line" d="M211 278 h14" stroke-width="1.2"/>
        <text class="contact" x="234" y="283">www.thefieldcrafters-example.co.uk</text>
      </g>
    </svg>
  </section>

</main>
</body>
</html>
```